Showroom Quote Web Application - Prism Layout wanted

This web app is an internal application that will be used by one of our customers to build quotes and produce orders of retail items with their customers

the overall design should use the colour pallet provided and have a clean and simple interface

we'd like to go with a prism layout type of look

attached mockups are just a rough stab at some layouts to give you an example, please feel free to reach out with any questions.

Please don't get hung up on the specific pages, they were intended to provide context, we are looking for a high level design using the provided colour schemes and fonts, additional work may follow for the selected designer when it comes to specific pages or work flows.

Sorry for the short timeline, we have a tight deadline on this one.

Target Market(s)

internal application for customer

Industry/Entity Type

Retail

Other font styles liked:
• see attached doc for fonts

Requirements
Must have
• simple and clean interface
• intuitive design
Nice to have
• see attached documents for logo colour schemes and fonts
• these must be incorporated into the design

```html
<!DOCTYPE html>
<html lang="en">
<head>
<meta charset="utf-8">
<title>Tapline Quote Studio – Member Login</title>
<link rel="stylesheet" href="https://fonts.googleapis.com/css2?family=Montserrat:wght@600;700&family=Source+Sans+3:wght@400;600;700&display=swap">
<style>
  :root {
    --gold-deep: #8f7440;
    --gold: #a98c55;
    --gold-light: #c2a877;
    --accent-text: #b08a4a;
    --navy: #0e3474;
    --white: #ffffff;
    --field: #efefef;
    --ink: #1d1d1f;
    --footer: #1c1c1e;
    --footer-icon: #2f2f31;
    --footer-text: #9a9a9a;
  }
  * { box-sizing: border-box; margin: 0; padding: 0; }
  html, body { width: 1200px; height: 800px; overflow: hidden; }
  body { font-family: "Source Sans 3", Arial, sans-serif; background: var(--footer); }

  .hero {
    position: relative;
    width: 1200px;
    height: 650px;
    overflow: hidden;
  }
  .hero-photo {
    position: absolute; inset: 0;
    background:
      radial-gradient(ellipse at 55% 80%, rgba(230,215,180,0.45), transparent 55%),
      radial-gradient(ellipse at 25% 35%, rgba(200,180,140,0.35), transparent 50%),
      linear-gradient(180deg, var(--gold-deep) 0%, var(--gold) 55%, var(--gold-light) 100%);
  }

  .brand {
    position: absolute; left: 105px; top: 44px;
    display: flex; align-items: center; gap: 8px;
    font-family: "Montserrat", Arial, sans-serif;
    font-weight: 700; font-size: 20px; color: var(--white);
  }
  .brand-square { width: 14px; height: 14px; background: var(--white); }

  .main-nav {
    position: absolute; top: 55px; right: 105px;
    display: flex; gap: 34px;
    font-family: "Montserrat", Arial, sans-serif;
    font-weight: 700; font-size: 10.5px; letter-spacing: 1.4px;
    color: var(--white);
  }
  .main-nav a { color: inherit; text-decoration: none; }

  .intro { position: absolute; left: 187px; top: 250px; width: 390px; color: var(--white); }
  .intro-title { font-weight: 700; font-size: 35px; line-height: 1.22; }
  .intro-text { margin-top: 56px; font-size: 14.5px; line-height: 1.55; }

  .login-card {
    position: absolute; left: 734px; top: 188px;
    width: 277px; height: 349px;
    background: var(--white); border-radius: 3px;
    padding: 42px 30px 0;
    text-align: center;
  }
  .login-title { font-weight: 700; font-size: 18px; letter-spacing: 0.6px; color: var(--ink); }
  .field {
    display: flex; align-items: center; justify-content: center;
    height: 48px; margin-top: 20px; border-radius: 24px;
    background: var(--field);
    font-family: "Montserrat", Arial, sans-serif;
    font-size: 10px; font-weight: 600; letter-spacing: 0.5px; color: #555;
  }
  .field + .field { margin-top: 17px; }
  .field.password { font-size: 16px; letter-spacing: 3px; color: #333; }
  .login-button {
    display: flex; align-items: center; justify-content: center;
    height: 48px; margin-top: 17px; border-radius: 24px;
    background: var(--navy); color: var(--white);
    font-family: "Montserrat", Arial, sans-serif;
    font-size: 10.5px; font-weight: 700; letter-spacing: 1.2px;
  }
  .forgot {
    display: block; margin-top: 28px;
    font-family: "Montserrat", Arial, sans-serif;
    font-size: 10px; font-weight: 600; letter-spacing: 1px;
    color: var(--accent-text); text-decoration: none;
  }

  .site-footer {
    height: 150px; background: var(--footer);
    text-align: center; padding-top: 32px;
  }
  .social { display: flex; justify-content: center; gap: 24px; }
  .social-dot { width: 36px; height: 36px; border-radius: 50%; background: var(--footer-icon); }
  .copyright { margin-top: 38px; font-size: 12.5px; color: var(--footer-text); }
</style>
</head>
<body>
  <header class="hero">
    <div class="hero-photo" role="img" aria-label="Photo of a plumbing showroom with basins, fittings and display walls under a warm gold tint"></div>

    <div class="brand"><span class="brand-square"></span>Tapline</div>

    <nav class="main-nav">
      <a href="#">MAIN</a>
      <a href="#">ABOUT</a>
      <a href="#">LOCATION</a>
      <a href="#">CONTACT US</a>
      <a href="#">SIGN UP</a>
    </nav>

    <section class="intro">
      <h1 class="intro-title">Tapline Quote<br>Studio</h1>
      <p class="intro-text">Lorem Ipsum is simply dummy text of the printing and typesetting industry. Lorem Ipsum has been the industry's standard dummy text ever since the 1500s.</p>
    </section>

    <form class="login-card">
      <h2 class="login-title">MEMBER LOGIN</h2>
      <div class="field">EMAIL ADRRESS</div>
      <div class="field password">••••••••••</div>
      <div class="login-button">LOG IN</div>
      <a class="forgot" href="#">FORGOT PASSWORD?</a>
    </form>
  </header>

  <footer class="site-footer">
    <div class="social">
      <span class="social-dot" role="img" aria-label="Social link"></span>
      <span class="social-dot" role="img" aria-label="Social link"></span>
      <span class="social-dot" role="img" aria-label="Social link"></span>
    </div>
    <p class="copyright">Copyright © 2017 Tapline Quote Studio. All rights reserved.</p>
  </footer>
</body>
</html>
```